Author/ Speaker Business Card design

I need a business card designed that will go with the branding that is already on my book and website. I like clean and straightforward, but I am not opposed to something more 'innovative'.

Target Market(s)

Colleges and Universities, educational institutions

Industry/Entity Type

Education

Contact Information for Business Card

Standard size. It should be able to be printed on good quality white or ivory paper.

Font styles to use
Sans Serif

Colors
0355a3

Requirements
Must have
• There's a blue on my website. It should have some blue. My logo is at the top. It should have the logo incorporated somewhere on it. My name, Author | Speaker | Teacher | Trainer, my phone number (+31 64-207 5184), my email address (milo@thebrightlearner.example), Social media icons (twitter, Instagram, LinkedIn) with the addresses (twitter @writermilohart, Instagram - thebrightlearner, LinkedIn - thebrightlearner) By they way, the website is www.thebrightlearner.example. There is a photo of the book on the website. Also, my full name is Milo Hart
Nice to have
• Try to use the font that is on the website and book. Also, if you could get that blue, that would be great.
Should not have
• My photo

```html
<!DOCTYPE html>
<html lang="en">
<head>
<meta charset="utf-8">
<title>Milo Hart – Business Card</title>
<link href="https://fonts.googleapis.com/css2?family=Montserrat:wght@400;600;700&display=swap" rel="stylesheet">
<style>
  :root {
    --page-bg: #d8d5d1;
    --card-bg: #eeeeec;
    --brand-blue: #0355a3;
    --brand-blue-deep: #143a86;
    --logo-tone: #e6dccb;
    --name-blue: #1d3f8c;
    --text-dark: #333438;
    --text-mid: #45474c;
  }
  * { margin: 0; padding: 0; box-sizing: border-box; }
  html, body {
    width: 1200px; height: 969px; overflow: hidden;
    background: var(--page-bg);
    font-family: "Montserrat", sans-serif;
  }
  .card {
    position: absolute; left: 100px; top: 200px;
    width: 1000px; height: 570px;
    background: var(--card-bg);
    border-radius: 24px;
    overflow: hidden;
    box-shadow: 0 10px 30px rgba(0,0,0,0.15);
  }
  .card-wave { position: absolute; inset: 0; }
  .brand {
    position: absolute; right: 64px; top: 100px;
    display: flex; align-items: center; gap: 18px;
    color: var(--logo-tone);
    font-weight: 600; font-size: 46px; letter-spacing: -0.5px;
  }
  .brand-dot { width: 34px; height: 34px; border-radius: 50%; background: var(--logo-tone); }
  .identity { position: absolute; left: 55px; top: 310px; }
  .identity-name {
    color: var(--name-blue); font-weight: 700; font-size: 38px;
    letter-spacing: 1px; text-transform: uppercase;
  }
  .identity-roles {
    margin-top: 6px; color: var(--text-dark);
    font-weight: 600; font-size: 20px;
  }
  .divider {
    position: absolute; left: 55px; top: 412px;
    width: 876px; height: 2px; background: var(--brand-blue);
  }
  .contact-list, .social-list {
    position: absolute; top: 434px; list-style: none;
    font-size: 22px; color: var(--text-mid); line-height: 30px;
  }
  .contact-list { left: 55px; }
  .social-list { right: 66px; text-align: right; }
  .contact-list li, .social-list li { display: flex; align-items: center; gap: 10px; }
  .social-list li { justify-content: flex-end; }
  .contact-icon { width: 22px; height: 22px; fill: var(--text-dark); flex: none; }
  .social-dot {
    width: 22px; height: 22px; border-radius: 50%;
    background: var(--text-dark); flex: none;
  }
</style>
</head>
<body>
  <div class="card">
    <svg class="card-wave" viewBox="0 0 1000 570" width="1000" height="570" aria-hidden="true">
      <defs>
        <linearGradient id="bandGradient" x1="0" y1="0" x2="1" y2="0">
          <stop offset="0" stop-color="var(--brand-blue-deep)"/>
          <stop offset="0.6" stop-color="var(--brand-blue)"/>
          <stop offset="1" stop-color="var(--brand-blue-deep)"/>
        </linearGradient>
      </defs>
      <path d="M60,0 H1000 V367 C860,362 730,325 610,255 C490,185 390,95 285,50 C200,18 120,4 60,0 Z" fill="url(#bandGradient)"/>
    </svg>

    <div class="brand">
      <span class="brand-dot"></span>
      <span class="brand-name">The Bright Learner</span>
    </div>

    <div class="identity">
      <h1 class="identity-name">Milo Hart</h1>
      <p class="identity-roles">Author | Speaker | Teacher | Trainer</p>
    </div>

    <div class="divider"></div>

    <ul class="contact-list">
      <li>
        <svg class="contact-icon" viewBox="0 0 24 24" aria-hidden="true"><path d="M6.6 10.8a15.1 15.1 0 0 0 6.6 6.6l2.2-2.2c.3-.3.7-.4 1-.2 1.1.4 2.3.6 3.6.6.6 0 1 .4 1 1V20c0 .6-.4 1-1 1A17 17 0 0 1 3 4c0-.6.4-1 1-1h3.5c.6 0 1 .4 1 1 0 1.3.2 2.5.6 3.6.1.3 0 .7-.2 1z"/></svg>
        <span>+31 64-207 5184</span>
      </li>
      <li>
        <svg class="contact-icon" viewBox="0 0 24 24" aria-hidden="true"><path d="M2 5h20v14H2z M3.5 6.5 12 13l8.5-6.5" fill="var(--text-dark)" stroke="var(--card-bg)" stroke-width="1.5"/></svg>
        <span>milo@thebrightlearner.example</span>
      </li>
      <li>
        <svg class="contact-icon" viewBox="0 0 24 24" aria-hidden="true"><circle cx="12" cy="12" r="10"/><path d="M2 12h20M12 2c3 3 3 17 0 20M12 2c-3 3-3 17 0 20" fill="none" stroke="var(--card-bg)" stroke-width="1.4"/></svg>
        <span>www.thebrightlearner.example</span>
      </li>
    </ul>

    <ul class="social-list">
      <li><span>@writermilohart</span><span class="social-dot"></span></li>
      <li><span>thebrightlearner</span><span class="social-dot"></span></li>
      <li><span>thebrightlearner</span><span class="social-dot"></span></li>
    </ul>
  </div>
</body>
</html>
```